Architecture firm needing a business card

We need a business card design for a new company based in the US called "Pellmore Architecture". Seeking minimalist designs that have a creativity/design feel but must be clean and professional. Please refer to the logo attached.

Target Market(s)

Real Estate Investors, Home Builders and Construction Firms.

Industry/Entity Type

Architecture

Contact Information for Business Card

Standard US size business cards. Would like to have some sort of graphic on the back side of the card - nothing that is too loud but something that may catch your attention. More or less grayscale colors that are in line with the logo colors (navy and greys essentially). Additional colors maybe accepted if blended properly (earthtones), but might be difficult to accomplish and maintain the clean/minimalist look.

Requirements
Must have
• Clean Lines
Nice to have
• some sort of graphics, would like to have something creative on the back side of the card
Should not have
• nothing too busy, cluttered or overwhelming.

```html
<!DOCTYPE html>
<html lang="en">
<head>
<meta charset="utf-8">
<title>Pellmore Architecture – Business Card</title>
<link rel="stylesheet" href="https://fonts.googleapis.com/css2?family=Lato:wght@300;400;700&display=swap">
<style>
  :root {
    --canvas: #e4e6e8;
    --card-white: #ffffff;
    --navy: #1d3f6e;
    --navy-deep: #17345d;
    --navy-light: #2f5a8f;
    --accent-blue: #4a78b5;
    --grey-text: #8a8f96;
    --body-text: #3a3f46;
  }
  * { box-sizing: border-box; margin: 0; padding: 0; }
  html, body {
    width: 1200px; height: 1120px; overflow: hidden;
    background: var(--canvas);
    font-family: "Lato", sans-serif;
  }
  .canvas { position: relative; width: 1200px; height: 1120px; }

  .card {
    position: absolute; left: 250px; width: 700px; height: 400px;
    box-shadow: 0 10px 30px rgba(30, 40, 55, 0.18);
    overflow: hidden;
  }

  /* Front */
  .card-front { top: 90px; background: var(--card-white); }
  .side-band-top {
    position: absolute; left: 0; top: 0; width: 24px; height: 58px;
    background: var(--accent-blue);
  }
  .side-band-bottom {
    position: absolute; left: 0; top: 150px; width: 24px; bottom: 0;
    background: var(--accent-blue);
  }
  .band-icons {
    position: absolute; left: 6px; bottom: 24px;
    display: flex; flex-direction: column; gap: 9px;
  }
  .band-icons svg { width: 12px; height: 12px; display: block; }
  .front-brand {
    position: absolute; left: 40px; top: 70px;
    display: flex; align-items: center; gap: 12px;
  }
  .brand-square {
    width: 34px; height: 34px; border: 3px solid var(--grey-text);
  }
  .brand-name {
    color: var(--navy); font-weight: 400; line-height: 1.05;
    font-size: 30px; letter-spacing: 0.5px;
  }
  .brand-name .brand-sub {
    display: block; font-size: 13px; letter-spacing: 5px; text-transform: uppercase;
  }
  .holder {
    position: absolute; right: 44px; top: 78px; text-align: right;
  }
  .holder-name {
    color: var(--navy); font-size: 26px; font-weight: 400; letter-spacing: 0.5px;
  }
  .holder-role { color: var(--grey-text); font-size: 17px; font-weight: 300; }
  .contact {
    position: absolute; left: 40px; bottom: 22px;
    color: var(--body-text); font-size: 14px; line-height: 21px;
  }

  /* Back */
  .card-back { top: 630px; }
  .back-field {
    position: absolute; inset: 0;
    background: linear-gradient(135deg, var(--navy-deep) 0%, var(--navy) 55%, var(--navy-light) 100%);
  }
  .back-brand {
    position: absolute; left: 56px; bottom: 96px;
    display: flex; align-items: center; gap: 14px;
  }
  .back-brand .brand-square { border-color: #ffffff; width: 40px; height: 40px; }
  .back-brand .brand-name { color: #ffffff; font-size: 40px; }
  .back-brand .brand-sub { font-size: 16px; letter-spacing: 7px; }
</style>
</head>
<body>
<div class="canvas">

  <section class="card card-front" aria-label="Card front">
    <div class="side-band-top"></div>
    <div class="side-band-bottom">
      <div class="band-icons">
        <svg viewBox="0 0 12 12" aria-label="phone"><path d="M3 1.5 4.8 3.3 3.9 4.6c.7 1.5 1.9 2.7 3.5 3.5l1.3-.9 1.8 1.8-1.3 1.5C5.6 10.3 1.7 6.4 1.5 2.8Z" fill="#fff"/></svg>
        <svg viewBox="0 0 12 12" aria-label="email"><rect x="1" y="2.5" width="10" height="7" fill="none" stroke="#fff" stroke-width="1.3"/><path d="M1.3 3 6 6.6 10.7 3" fill="none" stroke="#fff" stroke-width="1.3"/></svg>
        <svg viewBox="0 0 12 12" aria-label="location"><path d="M6 11.3S2 7 2 4.5a4 4 0 0 1 8 0C10 7 6 11.3 6 11.3Z" fill="#fff"/><circle cx="6" cy="4.5" r="1.4" fill="#4a78b5"/></svg>
      </div>
    </div>

    <div class="front-brand">
      <div class="brand-square"></div>
      <div class="brand-name">PELLMORE<span class="brand-sub">Architecture</span></div>
    </div>

    <div class="holder">
      <div class="holder-name">MAREN LOWE</div>
      <div class="holder-role">Manager</div>
    </div>

    <div class="contact">
      <p>+1 555 201 4478</p>
      <p>info@pellmore.com</p>
      <p>Po Box 3871, Alder Lane, USA</p>
    </div>
  </section>

  <section class="card card-back" aria-label="Card back">
    <div class="back-field" role="img" aria-label="Navy faceted geometric texture with a faint large brand mark in the upper right"></div>
    <div class="back-brand">
      <div class="brand-square"></div>
      <div class="brand-name">PELLMORE<span class="brand-sub">Architecture</span></div>
    </div>
  </section>

</div>
</body>
</html>
```